Life Coaching Business - needs business card design with logo

I need a business card and logo design for a life coaching business I started based in Los Angeles. I offer services to clients that wish to bring more balance and overall wholeness to their lives. As of right now, the business name is "Marcus Elwood Coaching." An iidea I had for the logo was to be kind of a Yin-Yang symbol but with dolphins, as the dolphin has symbolic meaning for my business. Although I am really open to other ideas as long as it incorporates the idea of “balance,” “wholeness,” and “dolphins.”I also wanted to incorporate the color blue, maybe in the form of water, waves, or some sort of peaceful imagery.

```html
<!DOCTYPE html>
<html lang="en">
<head>
<meta charset="utf-8">
<title>Marcus Elwood Coaching – Business Card</title>
<link rel="stylesheet" href="https://fonts.googleapis.com/css2?family=Raleway:wght@300;400;700&family=Open+Sans:wght@400&display=swap">
<style>
  :root {
    --backdrop: #5f5f5f;
    --card-white: #ffffff;
    --sky: #56b3e5;
    --deep: #2e8bc3;
    --ink: #2b2b2b;
    --text-grey: #3a3a3a;
    --icon: #5aaee0;
  }
  * { margin: 0; padding: 0; box-sizing: border-box; }
  html, body { width: 1200px; height: 1176px; overflow: hidden; }
  body { background: var(--backdrop); position: relative; font-family: "Raleway", sans-serif; }

  .card {
    position: absolute; left: 200px; width: 781px; height: 447px;
    border-radius: 22px; overflow: hidden;
    box-shadow: 0 4px 10px rgba(0,0,0,0.35);
  }
  .card--front { top: 55px; background: var(--card-white); }
  .card--back { top: 605px; background: var(--sky); }

  .card__water {
    position: absolute; left: 0; bottom: 0; width: 100%; height: 82px;
    background: linear-gradient(180deg, var(--deep) 0%, var(--sky) 100%);
  }

  .brand { position: absolute; display: flex; align-items: center; }
  .brand__circle { border-radius: 50%; flex: none; }
  .brand__words { font-family: "Raleway", sans-serif; font-weight: 400; line-height: 1; }
  .brand__name { display: block; white-space: nowrap; }
  .brand__tag { display: block; white-space: nowrap; }

  .card--front .brand { left: 76px; top: 181px; color: var(--sky); }
  .card--front .brand__circle { width: 84px; height: 84px; border: 3px solid var(--sky); margin-right: 12px; }
  .card--front .brand__name { font-size: 31px; }
  .card--front .brand__tag { font-size: 18px; margin-top: 9px; letter-spacing: 0.98em; }

  .card--back .brand { left: 155px; top: 160px; color: #ffffff; }
  .card--back .brand__circle { width: 118px; height: 118px; border: 3px solid #ffffff; margin-right: 26px; }
  .card--back .brand__name { font-size: 47px; }
  .card--back .brand__tag { font-size: 27px; margin-top: 12px; letter-spacing: 0.98em; }

  .person { position: absolute; left: 450px; top: 134px; }
  .person__name { font-size: 26px; color: var(--ink); letter-spacing: 0.01em; }
  .person__name strong { font-weight: 700; }
  .person__name span { font-weight: 300; }
  .person__title { font-size: 18px; color: var(--sky); margin-top: 2px; font-weight: 400; }

  .contacts { position: absolute; left: 450px; top: 210px; list-style: none; font-family: "Open Sans", sans-serif; font-size: 18.5px; color: var(--text-grey); }
  .contacts li { display: flex; align-items: center; height: 33px; }
  .contacts svg { width: 17px; height: 17px; margin-right: 11px; flex: none; }
</style>
</head>
<body>

<section class="card card--front">
  <div class="card__water" role="img" aria-label="Blue ocean wave decoration along the bottom edge"></div>

  <div class="brand">
    <span class="brand__circle"></span>
    <span class="brand__words">
      <span class="brand__name">Marcus Elwood</span>
      <span class="brand__tag">COACHING</span>
    </span>
  </div>

  <div class="person">
    <p class="person__name"><strong>YOUR</strong> <span>NAME</span></p>
    <p class="person__title">JOB TITLE</p>
  </div>

  <ul class="contacts">
    <li>
      <svg viewBox="0 0 16 16" aria-hidden="true"><path d="M1 6 C1 3 15 3 15 6 L12 7 L11 5 L5 5 L4 7 Z M3 8 L5 6 L11 6 L13 8 L13 13 L3 13 Z" fill="var(--icon)"/><circle cx="8" cy="9.5" r="1.8" fill="#fff"/></svg>
      000 000 0000
    </li>
    <li>
      <svg viewBox="0 0 16 16" aria-hidden="true"><rect x="1" y="3.5" width="14" height="9.5" fill="var(--icon)"/><path d="M1.5 4 L8 9 L14.5 4" fill="none" stroke="#fff" stroke-width="1.2"/></svg>
      youremail@xyz.com
    </li>
    <li>
      <svg viewBox="0 0 16 16" aria-hidden="true"><g fill="none" stroke="var(--icon)" stroke-width="1.1"><circle cx="8" cy="8" r="6.5"/><ellipse cx="8" cy="8" rx="3" ry="6.5"/><path d="M1.5 8 H14.5 M2.5 4.8 H13.5 M2.5 11.2 H13.5"/></g></svg>
      www.yourwebsite.com
    </li>
  </ul>
</section>

<section class="card card--back">
  <div class="brand">
    <span class="brand__circle"></span>
    <span class="brand__words">
      <span class="brand__name">Marcus Elwood</span>
      <span class="brand__tag">COACHING</span>
    </span>
  </div>
</section>

</body>
</html>
```